Vantrel Web Services

This is a new It services company operating in Perth western Australia

we need a website that is easy to navigate without a cluttered feel to it it should have the following links and pages

About Us
Services
Clients
Contact Us
MY Vantrel (login for clients)

Hi it is a web based IT services company so we would expect customers to come to the website for 2 different purposes the first is to enquire about our services and then as they become customers come to our website to manage their services so whilst they are seperate we want do not want it to look like 2 different websites

hope this helps

Hi to update this we need a home page and templates for sub pages

this is a design brief only and not the coding of the pages or building of the site

```html
<!DOCTYPE html>
<html lang="en">
<head>
<meta charset="utf-8">
<title>Vantrel Web Services</title>
<link href="https://fonts.googleapis.com/css2?family=Open+Sans:ital,wght@0,400;0,600;0,700;1,400&family=Source+Sans+3:wght@400;600;700&display=swap" rel="stylesheet">
<style>
:root{
  --crimson:#a5102d;
  --crimson-dark:#7e0b22;
  --navy:#26398f;
  --ink:#1e1e1e;
  --grey:#8a8a8a;
  --logo-grey:#a9a9a9;
  --white:#ffffff;
}
*{margin:0;padding:0;box-sizing:border-box}
html,body{width:761px;height:1200px;overflow:hidden;background:var(--white)}
body{position:relative;font-family:"Open Sans",Arial,sans-serif;color:var(--ink)}
.abs{position:absolute}

/* header */
.site-header{position:absolute;left:0;top:0;width:761px;height:56px;background:var(--white)}
.brand{position:absolute;left:138px;top:15px;display:flex;align-items:center;gap:6px}
.brand-dot{width:26px;height:26px;border-radius:50%;background:var(--crimson)}
.brand-name{font-family:"Source Sans 3",sans-serif;font-weight:700;font-size:17px;color:var(--crimson);letter-spacing:.5px}
.main-nav{position:absolute;top:22px;left:302px;display:flex;font-size:7.2px;text-transform:uppercase}
.main-nav a{color:var(--ink);text-decoration:none;height:15px;line-height:15px;padding:0 10px 0 0}
.main-nav a.is-active{background:var(--crimson);color:var(--white);border-radius:8px;padding:0 10px;margin-right:6px}
.main-nav a.gap{margin-right:10px}

/* hero */
.hero{position:absolute;left:0;top:56px;width:761px;height:319px;
  background:linear-gradient(180deg,#aab3bb 0%,#8d9aa6 35%,#6c7a70 55%,#3f5870 70%,#33495f 100%)}
.hero-title{position:absolute;left:136px;top:116px;font-family:"Source Sans 3",sans-serif;font-weight:700;font-size:27px;line-height:29px;color:var(--white);letter-spacing:-.6px}
.btn-signup{position:absolute;left:137px;top:186px;width:138px;height:28px;background:var(--crimson);color:var(--white);font-family:"Source Sans 3",sans-serif;font-weight:700;font-size:11.5px;display:flex;align-items:center;justify-content:center;gap:7px}
.hero-or{position:absolute;left:291px;top:196px;font-size:7px;color:var(--white)}
.btn-learn{position:absolute;left:332px;top:197px;width:40px;height:8px;border-radius:4px;background:#2d46b5;color:var(--white);font-size:4.5px;line-height:8px;text-align:center}
.hero-devices{position:absolute;left:390px;top:99px;width:262px;height:136px;border-radius:6px;background:linear-gradient(135deg,#2b2b2b,#7a6a5c 60%,#d8d8d8)}

/* intro */
.welcome{position:absolute;left:160px;top:425px;width:441px;text-align:center;font-size:9.4px;line-height:11.6px}
.dots{position:absolute;left:349px;width:82px;border-top:1px dotted #7c86b8}
.section-title{position:absolute;left:0;width:761px;text-align:center;font-family:"Source Sans 3",sans-serif;font-weight:700;font-size:20px;color:var(--navy);letter-spacing:-.4px}
.section-sub{position:absolute;left:0;width:761px;text-align:center;font-size:8px}

/* services */
.service-card{position:absolute;top:588px;width:119px;text-align:center}
.service-photo{width:119px;height:65px}
.service-caption{font-size:6px;margin-top:7px}
.service-btn{display:inline-block;margin-top:4px;width:35px;height:8px;border-radius:4px;background:#111;color:var(--white);font-size:4.5px;line-height:8px}
.service-btn.is-active{background:var(--crimson)}

/* work */
.work-tile{position:absolute;top:821px;width:187px;height:187px}
.work-label{position:absolute;left:0;bottom:0;width:100%;height:28px;background:rgba(25,35,60,.55);color:var(--white);font-size:11px;line-height:28px;text-align:center}
.tile-blue{background:linear-gradient(160deg,#8fb7d6 0%,#3b8fd0 40%,#0f74c8 70%,#1d4f8a 100%)}
.tile-warm{background:linear-gradient(160deg,#4a3a2c 0%,#8a5b3a 45%,#3a2c22 100%)}

/* clients */
.client{position:absolute;top:1054px;font-family:"Source Sans 3",sans-serif;font-weight:700;font-size:12px;color:var(--logo-grey);text-align:center}

/* footer */
.site-footer{position:absolute;left:0;top:1107px;width:761px;height:93px;background:var(--crimson)}
.foot-col{position:absolute;top:30px;font-size:6.6px;line-height:11.4px;color:var(--white)}
.social{position:absolute;top:30px;width:28px;height:28px;border-radius:50%;background:var(--crimson-dark)}
.btn-touch{position:absolute;left:428px;top:34px;width:79px;height:16px;border-radius:8px;background:#2433a6;color:var(--white);font-weight:700;font-size:7px;line-height:16px;text-align:center}
.foot-email{position:absolute;left:429px;top:54px;font-size:6.5px;font-style:italic;color:var(--white)}
.foot-copy{position:absolute;left:520px;top:38px;font-size:6.6px;color:var(--white)}
</style>
</head>
<body>

<header class="site-header">
  <div class="brand"><span class="brand-dot"></span><span class="brand-name">VANTREL</span></div>
  <nav class="main-nav">
    <a class="is-active" href="#">Home</a>
    <a class="gap" href="#">About Us</a>
    <a class="gap" href="#">Services</a>
    <a class="gap" href="#">Clients</a>
    <a class="gap" href="#">Contact Us</a>
    <a href="#">MY Vantrel</a>
  </nav>
</header>

<section class="hero" role="img" aria-label="Blurred city skyline across a river">
  <h1 class="hero-title">Lorem Ipsum Vantrel<br>Donor Smet Sit elit...</h1>
  <a class="btn-signup">SIGNUP ITS FREE
    <svg width="8" height="8" viewBox="0 0 8 8"><path d="M0 3h4V1l4 3-4 3V5H0z" fill="#fff"/></svg>
  </a>
  <span class="hero-or">-- or --</span>
  <span class="btn-learn">LEARN MORE</span>
  <div class="hero-devices" role="img" aria-label="Laptop and phone showing the website"></div>
</section>

<p class="welcome">Welcome text lorem ipsum dolor sit amet, consectetur adipisicing elit, sed do eiusmod tempor incididunt ut labore et dolore magna aliqua. Ut enim ad minim veniam, quis nostrud exercitation ullamco laboris nisi ut aliquip ex ea commodo consequat. Duis aute irure dolor</p>

<div class="dots" style="top:483px"></div>
<h2 class="section-title" style="top:497px">Our Services</h2>
<p class="section-sub" style="top:526px">Lorem ipsum dolor sit amet, consectetur adipisicing elit, sed do eiusmod tempor incididunt ut labore et dolore</p>
<div class="dots" style="top:553px"></div>

<div class="service-card" style="left:137px">
  <div class="service-photo" role="img" aria-label="Businessman touching digital interface" style="background:linear-gradient(135deg,#1b7fc4,#5fb6e6 60%,#2a3550)"></div>
  <p class="service-caption">Vantrel Lorem Dummy elit..</p>
  <span class="service-btn is-active">CLICK HERE</span>
</div>
<div class="service-card" style="left:260px">
  <div class="service-photo" role="img" aria-label="Colleagues working at a laptop" style="background:linear-gradient(135deg,#e9e4df,#b79c86 55%,#6b5444)"></div>
  <p class="service-caption">Vantrel Lorem Dummy elit..</p>
  <span class="service-btn">CLICK HERE</span>
</div>
<div class="service-card" style="left:382px">
  <div class="service-photo" role="img" aria-label="Team meeting in an office" style="background:linear-gradient(135deg,#e7ecef,#a9b6bf 55%,#5d6a74)"></div>
  <p class="service-caption">Vantrel Lorem Dummy elit..</p>
  <span class="service-btn">CLICK HERE</span>
</div>
<div class="service-card" style="left:504px">
  <div class="service-photo" role="img" aria-label="Hand on a computer mouse and keyboard" style="background:linear-gradient(135deg,#f4f4f4,#d9d9d9 60%,#bdbdbd)"></div>
  <p class="service-caption">Vantrel Lorem Dummy elit..</p>
  <span class="service-btn">CLICK HERE</span>
</div>

<h2 class="section-title" style="top:742px">Our Work</h2>
<p class="section-sub" style="top:769px;color:var(--grey);font-size:7.6px">Lorem ipsum dolor sit amet, consectetur adipisicing elit, sed do eiusmod tempor incididunt.</p>
<div class="abs" style="left:349px;top:794px;width:64px;border-top:1px solid #ddd"></div>

<div class="work-tile tile-blue" style="left:0" role="img" aria-label="Hotel campaign with beach scene"><div class="work-label">Lorem Title</div></div>
<div class="work-tile tile-warm" style="left:191px" role="img" aria-label="Happy hour promotion with drinks"><div class="work-label">Lorem Title</div></div>
<div class="work-tile tile-blue" style="left:383px" role="img" aria-label="Hotel campaign with beach scene"><div class="work-label">Lorem Title</div></div>
<div class="work-tile tile-warm" style="left:574px" role="img" aria-label="Happy hour promotion with drinks"><div class="work-label">Lorem Title</div></div>

<span class="client" style="left:137px">KORVANE</span>
<span class="client" style="left:238px;font-weight:400">Halbrook Ellis</span>
<span class="client" style="left:352px">Quillstead</span>
<span class="client" style="left:462px;font-weight:400">Tessaline</span>
<span class="client" style="left:560px">Marrowgate</span>

<footer class="site-footer">
  <div class="foot-col" style="left:137px">Home<br>About Us<br>Services</div>
  <div class="foot-col" style="left:186px">Clients<br>Contact Us<br>Help</div>
  <div class="foot-col" style="left:238px">My Vantrel<br>Register Vantrel<br>Newsletter</div>
  <span class="social" style="left:316px" aria-label="Social profile"></span>
  <span class="social" style="left:347px" aria-label="Social profile"></span>
  <span class="social" style="left:378px" aria-label="Social profile"></span>
  <span class="btn-touch">GET IN TOUCH</span>
  <span class="foot-email">Email : info@vantrel.com</span>
  <span class="foot-copy">© 2014 &nbsp;- &nbsp;Terms and Conditions</span>
</footer>

</body>
</html>
```